English and Spanish Language School Needs a Business Card

Need a business card design a startup company called Corvelle Language School. The company will offer English and Spanish conversational level courses designed to make the learner feel comfortable with grammar and vocabulary. We would like to see a logo with some colour that should communicate learning, growth.

Target Market(s)

Consumers and businesses

Industry/Entity Type

Education

Contact Information for Business Card

TBD

Font styles to use
Serif

Requirements
Must have
• Include the following
• Logo
• Name
• Title
• Cellphone Number
• Office Phone number
• Email address
• Office Address

```html
<!DOCTYPE html>
<html lang="en">
<head>
<meta charset="utf-8">
<title>Corvelle Language School – Business Card</title>
<link rel="stylesheet" href="https://fonts.googleapis.com/css2?family=Montserrat:wght@400;600&display=swap">
<style>
  :root {
    --page: #e9e6e2;
    --card-top: #21332f;
    --card-bottom: #0d1614;
    --accent: #d42a35;
    --accent-faint: rgba(120, 30, 36, 0.55);
    --ink: #f2f2f2;
    --shadow: rgba(0, 0, 0, 0.35);
  }
  * { margin: 0; padding: 0; box-sizing: border-box; }
  html, body {
    width: 1200px; height: 913px; overflow: hidden;
    background: var(--page);
    font-family: "Montserrat", Arial, sans-serif;
  }
  .sheet { position: relative; width: 1200px; height: 913px; }
  .card {
    position: absolute; top: 300px;
    width: 540px; height: 310px;
    border-radius: 18px;
    background: linear-gradient(160deg, var(--card-top) 0%, var(--card-bottom) 100%);
    box-shadow: 0 14px 30px var(--shadow);
    color: var(--ink);
    overflow: hidden;
  }
  .card--front { left: 40px; }
  .card--back { left: 620px; }

  .brand-name {
    position: absolute; left: 36px; bottom: 70px;
    width: 220px;
    font-weight: 600; font-size: 30px; line-height: 1.1;
    color: var(--accent);
  }
  .contact {
    position: absolute; left: 300px; top: 70px;
    font-size: 13px; line-height: 1.55;
  }
  .contact__name { font-weight: 600; font-size: 19px; color: var(--accent); line-height: 1.2; }
  .contact__title { font-size: 12px; color: var(--accent); margin-bottom: 8px; }
  .contact__address { margin-bottom: 4px; }
  .contact__row { display: flex; align-items: center; gap: 8px; }
  .contact__row svg { width: 11px; height: 11px; flex: none; }
  .contact__web { font-weight: 600; }

  .brand-name--faint {
    left: 0; right: 0; bottom: auto; top: 88px; width: auto;
    text-align: center; font-size: 46px; color: var(--accent-faint);
  }
  .back-web {
    position: absolute; right: 34px; bottom: 36px;
    font-size: 14px; font-weight: 600; color: var(--ink);
  }
</style>
</head>
<body>
<main class="sheet">
  <section class="card card--front">
    <div class="brand-name">Corvelle Language School</div>
    <div class="contact">
      <div class="contact__name">Marcus Whitfield</div>
      <div class="contact__title">Director</div>
      <div class="contact__address">Po Box 218<br>Ashgrove VIC 3927</div>
      <div class="contact__row">
        <svg viewBox="0 0 12 12"><rect x="3" y="1" width="6" height="10" rx="1" fill="none" stroke="#d42a35" stroke-width="1.3"/></svg>
        +330 2718-4093
      </div>
      <div class="contact__row">
        <svg viewBox="0 0 12 12"><path d="M2 1.5 L4.5 1.5 L5.2 4 L3.8 5 Q5 7.5 7 8.2 L8 6.8 L10.5 7.5 L10.5 10 Q5 10.5 2 4 Z" fill="#d42a35"/></svg>
        +330 2739-6152
      </div>
      <div class="contact__row">
        <svg viewBox="0 0 12 12"><rect x="1" y="2.5" width="10" height="7" fill="none" stroke="#d42a35" stroke-width="1.2"/><path d="M1 2.5 L6 6.5 L11 2.5" fill="none" stroke="#d42a35" stroke-width="1.2"/></svg>
        hello@corvelleschool.com
      </div>
      <div class="contact__row contact__web">
        <svg viewBox="0 0 12 12"><circle cx="6" cy="6" r="4.8" fill="none" stroke="#d42a35" stroke-width="1.2"/><ellipse cx="6" cy="6" rx="2" ry="4.8" fill="none" stroke="#d42a35" stroke-width="1"/><line x1="1.2" y1="6" x2="10.8" y2="6" stroke="#d42a35" stroke-width="1"/></svg>
        corvelleschool.com
      </div>
    </div>
  </section>

  <section class="card card--back">
    <div class="brand-name brand-name--faint">Corvelle Language School</div>
    <div class="back-web">www.corvelleschool.com</div>
  </section>
</main>
</body>
</html>
```